Wordpress Design for Fruit & Veggie Swap Site

I need a wordpress design for the HOME PAGE of a company located in Kona, Hawaii called Leaf Loop Hawaii. Leaf Loop Hawaii (LLH) is a site intended to support the local food movement by connecting neighbors in order for them to swap/trade produce from their farm or garden. The purpose of this site is to support sustainable agriculture in Hawaii and encourage community interaction.

The model of the site is similar to:
http://www.harvtrade.me/ (I really like the simple design of this site)
http://www.plotbarter.co.uk/ (I don't like the design of this site, just the functionality. The design is too busy and unbalanced.)
Unlike the two sites listed above, however, LLH is only targeted at people living on the Big Island of Hawaii.

The site is simply intended to be a platform to connect people, then they are free to swap or barter off site, similar to the way tradeboard connects people. Users can create "posts" for crops that they have available for swap, which are searchable based on name and location.

I have created a very basic, no-css, dev version of the site to work on the back end, which is located here: http://leafloophawaii.com/test
Feel free to register and create a test post to get a feel for how it works.

The images I have uploaded are just for ideas and do not have to be in the design.
Updates

Reason: I extended the deadline so you have more time to work on designs. Thank you!

Target Market(s)

The targeted audience is gardeners and farmers on the Big Island of Hawaii. These people are quite varied in age and technical ability.

Industry/Entity Type

Agriculture

Requirements
Must have
• On the homepage, I would like to have a list of the most recent "posts", displayed as the post title, with the most recent post at the top of the list. In the test site, this is located in the right column, but it doesn't have to be in that location in the final design.

I would also like the option to "Add new listing" to be displayed creatively on the home page. This can be in the form of a graphic that links to a form on another page.

I would also like to have a search box on the homepage. Users can search by crop name and/or location.

The main focal point of the home page will be a Google map application of the Big Island. I am in the process of developing this. You can see the map on the test site, please keep in mind that this map may change slightly in future revisions. Feel free to change the size and styling of the map to fit your design.

I would like the homepage to have a simple and clean layout, making it clear to users how the site works.
For the graphics, I would like to incorporate the "crop circles" idea (yes, like the alien crop circles in fields) with fruits and veggies (including tropical fruit found in Hawaii like banana, coconut, lychee, taro, oranges, as well as traditional vegetables like carrots, lettuce, etc.), and also potentially with the idea of sharing and circulating produce with neighbors.
Please note that those specific fruits and veggies don't need to be used, or that many of them, I was just giving them as examples.

I would also like to have a place on the homepage where users can login/sign up. This can be a login form with a sign up link, or a login link and a sign up link.

I would like the entire design to fit on a page without having to scroll.

Once the site has a substantial user base, I plan to incorporate advertising. Please create a design that will be easy to integrate ads into in the future, most likely in the side bar or footer. I do not want the original design to have ad space, just the ability to add it easily in the future and having it look good with the current design.

```html
<!DOCTYPE html>
<html lang="en">
<head>
<meta charset="utf-8">
<title>Leaf Loop Hawaii</title>
<link href="https://fonts.googleapis.com/css2?family=Oswald:wght@300;400;500&display=swap" rel="stylesheet">
<style>
  :root {
    --bg-deep: #0d5a0c;
    --bg-mid: #2f8f1a;
    --bg-light: #6cc23a;
    --panel: #1f5f12;
    --panel-dark: #143f0b;
    --green-band: #3aa312;
    --green-lite: #8fd44a;
    --posts-bg: rgba(84, 176, 34, 0.88);
    --white: #ffffff;
    --red: #d8173a;
    --mustard: #c8b000;
    --blue: #3a6fc0;
    --search-btn: #1d9bd6;
    --search-text: #4a5a72;
    --map-tone-a: #b4c9e3;
    --map-tone-b: #a3bcdc;
  }
  * { margin: 0; padding: 0; box-sizing: border-box; }
  html, body { width: 1200px; height: 900px; overflow: hidden; }
  body { font-family: "Oswald", sans-serif; color: var(--white); position: relative; }

  .backdrop {
    position: absolute; inset: 0;
    background: radial-gradient(ellipse at 40% 20%, var(--bg-light) 0%, var(--bg-mid) 35%, var(--bg-deep) 80%);
  }
  .site {
    position: absolute; left: 88px; top: 201px; width: 1024px; height: 513px;
    background: linear-gradient(135deg, #2c6d1a 0%, var(--panel) 50%, var(--panel-dark) 100%);
  }

  .brand-mark { position: absolute; left: 197px; top: 222px; width: 98px; text-align: center; }
  .brand-mark .dot { width: 60px; height: 60px; border-radius: 50%; background: var(--green-lite); margin: 0 auto 6px; }
  .brand-mark .name { font-size: 22px; font-weight: 400; color: var(--white); letter-spacing: 2px; }

  .site-title { position: absolute; left: 418px; top: 236px; font-size: 46px; font-weight: 400; line-height: 60px; white-space: nowrap; }
  .site-title .region { font-size: 28px; color: var(--green-lite); margin-left: 10px; }
  .tagline { position: absolute; left: 418px; top: 298px; font-size: 17px; font-weight: 400; letter-spacing: .3px; line-height: 24px; }

  .search { position: absolute; left: 124px; top: 346px; width: 240px; height: 34px; display: flex; }
  .search .field { flex: 1; background: var(--white); color: var(--search-text); font-size: 20px; padding: 0 9px; line-height: 32px; }
  .search .go { width: 30px; background: var(--search-btn); display: flex; align-items: center; justify-content: center; }

  .nav { position: absolute; top: 404px; height: 26px; font-size: 13px; line-height: 26px; text-align: center; }
  .nav.how { left: 96px; width: 91px; background: var(--red); }
  .nav.faq { left: 193px; width: 92px; background: var(--mustard); }
  .nav.contact { left: 291px; width: 88px; background: var(--blue); }

  .account-band { position: absolute; left: 72px; top: 454px; width: 318px; height: 46px; background: var(--green-band);
    display: flex; align-items: center; padding-left: 76px; gap: 33px; font-size: 14px; letter-spacing: 4px; line-height: 46px; }
  .account-band span { display: flex; align-items: center; gap: 10px; }
  .fold { position: absolute; left: 72px; top: 446px; width: 0; height: 0; border-left: 16px solid transparent; border-bottom: 8px solid #0c3306; }

  .new-circle { position: absolute; left: 115px; top: 501px; width: 274px; height: 186px; border-radius: 0 0 4px 4px;
    background: linear-gradient(120deg, #7a9b3a, #4f7f24 50%, #6e8a2c); }
  .new-circle .card { position: absolute; left: 6px; top: 11px; width: 259px; height: 163px; background: rgba(96, 190, 40, .8);
    display: flex; align-items: flex-start; padding: 50px 0 0 26px; gap: 34px; }
  .new-circle .bars { display: flex; flex-direction: column; gap: 10px; padding-top: 4px; }
  .new-circle .bars i { display: block; width: 79px; height: 9px; background: var(--white); }
  .new-circle .label { font-size: 30px; line-height: 30px; font-weight: 400; margin-top: -4px; }

  .map { position: absolute; left: 417px; top: 345px; width: 393px; height: 343px;
    background: linear-gradient(160deg, var(--map-tone-a), var(--map-tone-b)); }

  .posts-heading { position: absolute; left: 857px; top: 244px; font-size: 22px; letter-spacing: 7.5px; font-weight: 400;
    border-bottom: 2px solid var(--white); line-height: 28px; }
  .posts { position: absolute; left: 833px; top: 296px; width: 258px; height: 379px; background: var(--posts-bg);
    list-style: none; padding: 19px 18px 0 25px; font-size: 12.5px; line-height: 24px; }
  .all { position: absolute; left: 1022px; top: 687px; width: 94px; height: 26px; background: var(--green-band);
    font-size: 13px; letter-spacing: 3px; text-align: center; line-height: 26px; }
</style>
</head>
<body>
  <div class="backdrop" role="img" aria-label="Blurred close-up of a green leaf with water droplets"></div>
  <div class="site" role="img" aria-label="Dark green mosaic of fruit and vegetable photographs"></div>

  <div class="brand-mark"><div class="dot"></div><div class="name">LLH</div></div>

  <h1 class="site-title">LEAF LOOP<span class="region">HAWAII</span></h1>
  <p class="tagline">CONECTING NEIGHBOURS FOR LOCAL FOOD EXCHANGE</p>

  <div class="search">
    <div class="field">search for...</div>
    <div class="go">
      <svg width="16" height="16" viewBox="0 0 16 16"><circle cx="6" cy="6" r="4.5" fill="none" stroke="#fff" stroke-width="2"/><line x1="9.5" y1="9.5" x2="14.5" y2="14.5" stroke="#fff" stroke-width="2.5"/></svg>
    </div>
  </div>

  <div class="nav how">HOW IT WORKS</div>
  <div class="nav faq">FAQ</div>
  <div class="nav contact">CONTACT</div>

  <div class="fold"></div>
  <div class="account-band">
    <span><svg width="16" height="16" viewBox="0 0 16 16"><circle cx="8" cy="4.5" r="4" fill="#fff"/><path d="M0 16 Q0 9 8 9 Q16 9 16 16Z" fill="#fff"/></svg>LOGIN</span>
    <span><svg width="11" height="11" viewBox="0 0 11 11"><rect x="4" y="0" width="3" height="11" fill="#fff"/><rect x="0" y="4" width="11" height="3" fill="#fff"/></svg>REGISTER</span>
  </div>

  <div class="new-circle" role="img" aria-label="Photo collage of fresh produce">
    <div class="card">
      <div class="bars"><i></i><i></i><i></i></div>
      <div class="label">NEW<br>CIRCLE</div>
    </div>
  </div>

  <div class="map" role="img" aria-label="Interactive map of the Big Island of Hawaii with produce post markers"></div>

  <h2 class="posts-heading">RECENT POSTS</h2>
  <ul class="posts">
    <li>testing redirect 3 (Honaunau)</li>
    <li>testing redirect 2 (Honaunau)</li>
    <li>testing redirect (Volcano)</li>
    <li>Testing no street address (Milolii)</li>
    <li>Lemons (Pahala)</li>
    <li>Oranges (Kohala)</li>
    <li>Coconuts (hilo)</li>
    <li>Lettuce (Holualoa)</li>
    <li>Testuser trying to add photo (Hawi)</li>
    <li>New post from testuser with map and photo (honokaa)</li>
    <li>New post from testuser (honokaa)</li>
    <li>Papaya seedlings (captain cook)</li>
  </ul>
  <div class="all">&lt; ALL &gt;</div>
</body>
</html>
```